Chocoloate confectionery company requires vibrant Packaging Design for a mini chocolate bar

- Need a packaging design for a new product; a chocolate mini-bar.
- Our corporate colors of brown and pink should be included in design.
- The chocolate weighs 20grams and measures 8 cm length x 5 cm width x 1 cm depth
- It will be covered in gold foil and wrapped in a paper sleeve.
- The paper sleeve measures 13.5 cm length x 7.5 cm width
- The paper sleeve can then be sectioned into 3 equal areas
- The packaging design is required on middle section of the sleeve.
- The ingredients, company details, barcode and disclaimer etc will be on the right section
- The left section of the sleeve may be left blank

PLEASE SEE SAMPLE PICTURES PER ATTACHED

Target Market(s)

Everyday shoppers (e.g. Moms, Dads, kids, teens, students)

Industry/Entity Type

It Company

Requirements
Must have
• Brown and pink colors (as per business card attached)
Name of mini chocolate bar is Mallow Nib. This must appear on middle section of paper sleeve

```html
<!DOCTYPE html>
<html lang="en">
<head>
<meta charset="utf-8">
<title>Mallow Nib — mini bar sleeve</title>
<link rel="stylesheet" href="https://fonts.googleapis.com/css2?family=Barlow:wght@600;800&family=Barlow+Semi+Condensed:wght@400&display=swap">
<style>
  :root {
    --sleeve: #231f20;
    --fold: #57514f;
    --gold-dark: #b8922a;
    --gold-mid: #d9b948;
    --gold-light: #f1dc7e;
    --logo: #d8d5d2;
    --accent-pink: #c2418f;
    --tagline: #a39e9b;
    --info: #8f8a87;
    --weight: #7d7875;
    --label: #ffffff;
    --page: #ffffff;
  }
  * { margin: 0; padding: 0; box-sizing: border-box; }
  html, body { width: 1200px; height: 667px; overflow: hidden; background: var(--page); }
  .sleeve-canvas {
    position: relative; width: 1200px; height: 667px; overflow: hidden;
    font-family: "Barlow", Arial, sans-serif;
  }
  .foil {
    position: absolute; left: 18px; width: 1172px;
    background: linear-gradient(90deg, var(--gold-mid), var(--gold-light) 20%, var(--gold-dark) 38%, var(--gold-light) 55%, var(--gold-mid) 72%, var(--gold-light) 88%, var(--gold-dark));
  }
  .foil--top { top: 0; height: 33px; }
  .foil--bottom { top: 625px; height: 35px; }
  .sleeve {
    position: absolute; left: 0; top: 33px; width: 1200px; height: 592px;
    background: var(--sleeve);
  }
  .fold-lines { position: absolute; left: 0; top: 0; }
  .rotated {
    position: absolute; transform: translate(-50%, -50%) rotate(-90deg);
    white-space: nowrap;
  }
  .net-weight {
    left: 447px; top: 68px; font-size: 17px; font-weight: 600; color: var(--weight);
  }
  .product-name {
    left: 612px; top: 335px; font-size: 72px; line-height: 1; font-weight: 800; color: var(--logo);
    letter-spacing: 0.5px;
  }
  .brand-mark {
    position: absolute; left: 598px; top: 84px; width: 28px; height: 28px;
    background: var(--accent-pink);
  }
  .tagline {
    left: 727px; top: 335px; font-family: "Barlow Semi Condensed", Arial, sans-serif;
    font-size: 20px; font-weight: 400; color: var(--tagline); letter-spacing: 1px;
  }
  .label-panel {
    position: absolute; left: 903px; top: 57px; width: 106px; height: 155px;
    background: var(--label);
  }
  .ingredients {
    position: absolute; left: 952px; top: 412px; width: 374px; height: 114px;
    transform: translate(-50%, -50%) rotate(90deg);
    font-family: "Barlow Semi Condensed", Arial, sans-serif;
    font-size: 13.5px; line-height: 19px; color: var(--info); letter-spacing: 0.2px;
    white-space: nowrap;
  }
  .rating { position: absolute; left: 1055px; top: 286px; }
</style>
</head>
<body>
<main class="sleeve-canvas">
  <div class="foil foil--top"></div>
  <div class="foil foil--bottom"></div>

  <section class="sleeve">
    <svg class="fold-lines" width="1200" height="592" aria-hidden="true">
      <line x1="400" y1="15" x2="400" y2="580" stroke="var(--fold)" stroke-width="1" stroke-dasharray="7 6"/>
      <line x1="800" y1="15" x2="800" y2="580" stroke="var(--fold)" stroke-width="1" stroke-dasharray="7 6"/>
    </svg>
  </section>

  <div class="rotated net-weight">20g</div>
  <h1 class="rotated product-name">Mallow Nib</h1>
  <div class="brand-mark" aria-hidden="true"></div>
  <p class="rotated tagline">~ hand made chocolate ~</p>

  <div class="label-panel"></div>

  <p class="ingredients">
    Ingredients: Sugar, suffer hydrogenated vegetable<br>
    fats (Palm Kernal), maltedextrin, low fat coca powder,<br>
    wheat, powder (milk), leathin, flavouring, elulsifier.<br>
    Allergins: Contains cows milk, soya beans, may<br>
    contain tree nuts.<br>
    Hand made in Zimbabwe.
  </p>

  <svg class="rating" width="18" height="74" viewBox="0 0 18 74" aria-label="Three stars">
    <g fill="var(--weight)">
      <polygon points="9,1 11.2,6.5 17,6.8 12.5,10.5 14,16 9,12.9 4,16 5.5,10.5 1,6.8 6.8,6.5"/>
      <polygon points="9,29 11.2,34.5 17,34.8 12.5,38.5 14,44 9,40.9 4,44 5.5,38.5 1,34.8 6.8,34.5"/>
      <polygon points="9,57 11.2,62.5 17,62.8 12.5,66.5 14,72 9,68.9 4,72 5.5,66.5 1,62.8 6.8,62.5"/>
    </g>
  </svg>
</main>
</body>
</html>
```